GUARANTEED! Simple website for independent event planner and consultant...

I need a website that is no more than 5 or 6 pages to illustrate who I am and what I can offer to groups who book hotels for meetings and conferences. I have 20 years of experience planning meetings within hotels and I am now ready to go out on my own and help clients choose venues, negotiate contracts and plan effective meetings. I will focus on clients planning meetings in the mountains of Colorado but I am willing to travel as well. I want to work with a person who is collaborative and can direct me on what they need to move the project along quickly. I already have my logo, a hosting site and work e-mail address. Also, I recently hired a photographer to do head shots. Lastly, it important for me to be able to talk on the phone or skype with this person, as needed and I must be able to make changes to my site down the road when necessary...

Target Market(s)

Corporate Groups

Industry/Entity Type

Event Planning

Coding

Coded - Design and coding required

Number of Pages Required

5+ page

Font styles to use
Sans Serif

Requirements
Must have
• About me page, event planning services offered page, task force and consulting work page, testimonials page, page for blogs, page to contact me/request a proposal. May need advice on what else I need...
Nice to have
• I want it to look sharp and professional. I want people to look at my site and know immediately that they can trust me and the work I can do.
• I don't want it to look like it is over the top as I am not a HUGE company but I do want it to be professional and easy to view and navigate.
Should not have
• Bright colors
• My logo is bright orange and black. I have also used dark grey and orange. See below:
• Orange:
• C = 0
• M = 64
• Y = 100
• K = 0
• Gray:
• C = 67
• M = 60
• Y = 59
• K = 45
• Font: Gotham Book and Gotham Bold

```html
<!DOCTYPE html>
<html lang="en">
<head>
<meta charset="utf-8">
<title>Summitway Event Management</title>
<link rel="stylesheet" href="https://fonts.googleapis.com/css2?family=Montserrat:wght@300;400;500;600;700&display=swap">
<style>
  :root {
    --orange: #f47b20;
    --charcoal: #25272b;
    --charcoal-deep: #1f2024;
    --panel-grey: #efeeec;
    --text-dark: #3b3b3d;
    --text-body: #55565a;
    --text-muted: #8c8e93;
    --white: #ffffff;
    --input-grey: #44464b;
  }
  * { box-sizing: border-box; margin: 0; padding: 0; }
  html, body { width: 1200px; height: 2871px; overflow: hidden; }
  body {
    position: relative;
    font-family: "Montserrat", Arial, sans-serif;
    background: var(--charcoal);
    color: var(--white);
  }
  .block, .photo { position: absolute; }

  /* Hero */
  .hero-photo { left: 0; top: 0; width: 1200px; height: 674px;
    background:
      radial-gradient(ellipse 520px 260px at 1000px 170px, rgba(235,236,228,.85), rgba(235,236,228,0) 70%),
      radial-gradient(ellipse 620px 200px at 260px 90px, rgba(200,204,190,.8), rgba(200,204,190,0) 75%),
      radial-gradient(ellipse 700px 300px at 420px 470px, #2a3a86, rgba(42,58,134,0) 80%),
      linear-gradient(180deg, #9aa293 0%, #3b4a8a 32%, #223076 60%, #1b2762 100%); }
  .brand { position: absolute; left: 159px; top: 64px; font-weight: 700; font-size: 23px;
    letter-spacing: .5px; color: var(--orange); }
  .menu-btn { position: absolute; left: 990px; top: 65px; width: 50px; height: 54px;
    background: var(--charcoal); display: flex; flex-direction: column; align-items: center; justify-content: center; }
  .menu-btn span { font-size: 7px; margin-top: 4px; letter-spacing: .5px; }
  .hero-card { left: 597px; top: 331px; width: 603px; height: 201px; background: var(--orange);
    padding: 10px 0 0 26px; }
  .hero-card h1 { font-weight: 300; font-size: 45px; line-height: 54px; letter-spacing: -.3px; }
  .hero-card p { font-size: 21px; line-height: 34px; margin-top: 6px; }

  /* About */
  .about-photo { left: 0; top: 674px; width: 599px; height: 375px;
    background:
      radial-gradient(ellipse 180px 230px at 300px 300px, #2a2b2f, rgba(42,43,47,0) 80%),
      linear-gradient(180deg, #8f9a84 0%, #6f7e66 45%, #4d5a4a 100%); }
  .about-panel { left: 599px; top: 674px; width: 601px; height: 375px; background: var(--panel-grey);
    padding: 84px 0 0 44px; color: var(--text-dark); }
  .label { font-weight: 600; font-size: 15px; letter-spacing: 1px; }
  .about-panel p { font-size: 21px; line-height: 27px; margin-top: 26px; width: 340px; color: var(--text-body); }

  /* Why */
  .why-panel { left: 0; top: 1049px; width: 599px; height: 387px; background: var(--orange); padding: 93px 0 0 158px; }
  .why-panel p { font-size: 21px; line-height: 27px; margin-top: 22px; width: 380px; }
  .btn { display: inline-flex; align-items: center; justify-content: center; border: 2px solid currentColor;
    border-radius: 22px; font-size: 13px; letter-spacing: .5px; }
  .why-panel .btn { margin-top: 36px; width: 210px; height: 41px; }
  .why-photo { left: 599px; top: 1049px; width: 301px; height: 387px;
    background:
      radial-gradient(ellipse 130px 110px at 190px 220px, #e9e8e4, rgba(233,232,228,0) 80%),
      linear-gradient(180deg, #a9a49c 0%, #9b968e 50%, #8f8a83 100%); }
  .why-fill { left: 900px; top: 1049px; width: 300px; height: 387px; background: var(--orange); }

  /* Gallery */
  .g1 { left: 0; top: 1436px; width: 300px; height: 386px;
    background: radial-gradient(ellipse 200px 260px at 110px 170px, #a8642a, rgba(168,100,42,0) 80%), linear-gradient(180deg, #3a2414, #24170f); }
  .g2 { left: 300px; top: 1436px; width: 299px; height: 386px;
    background: linear-gradient(180deg, #d4d5d1 0%, #c7c9c4 30%, #3a4a44 55%, #5e5a52 100%); }
  .g3 { left: 599px; top: 1436px; width: 301px; height: 386px;
    background: radial-gradient(ellipse 220px 120px at 150px 190px, #e0a46a, rgba(224,164,106,0) 80%), linear-gradient(180deg, #4a2e24 0%, #7a5a3e 55%, #5c4a2c 100%); }
  .g4 { left: 900px; top: 1436px; width: 300px; height: 386px;
    background: radial-gradient(ellipse 170px 150px at 170px 250px, #d59a5a, rgba(213,154,90,0) 80%), linear-gradient(180deg, #20386e 0%, #2b4580 55%, #1c1a22 100%); }

  /* Blog */
  .blog-left { left: 0; top: 1822px; width: 300px; height: 676px; background: var(--charcoal); }
  .blog-art { left: 300px; top: 1822px; width: 900px; height: 676px;
    background:
      radial-gradient(ellipse 260px 200px at 620px 200px, rgba(70,150,205,.55), rgba(70,150,205,0) 80%),
      radial-gradient(ellipse 230px 160px at 560px 560px, rgba(240,160,40,.55), rgba(240,160,40,0) 80%),
      linear-gradient(180deg, #b2a19a, #a8968f); }
  .blog-card { left: 300px; top: 1822px; width: 299px; height: 375px; background: var(--charcoal-deep); padding: 106px 0 0 45px; }
  .blog-card h2 { color: var(--orange); font-weight: 700; font-size: 17px; letter-spacing: .5px; }
  .blog-card h3 { color: var(--orange); font-weight: 600; font-size: 11.5px; margin-top: 8px; }
  .blog-card p { font-size: 13px; line-height: 17px; margin-top: 16px; width: 200px; }
  .blog-card .btn { color: var(--orange); margin-top: 26px; width: 134px; height: 37px; font-size: 12px; }

  /* Footer */
  .footer { left: 0; top: 2498px; width: 1200px; height: 373px; background: var(--charcoal); }
  .foot-brand { position: absolute; left: 159px; top: 50px; font-weight: 700; font-size: 17px; letter-spacing: .5px; }
  .foot-about { position: absolute; left: 159px; top: 90px; width: 205px; font-size: 9px; line-height: 16px; color: var(--text-muted); }
  .copyright { position: absolute; left: 159px; top: 314px; font-size: 9.5px; color: var(--text-muted); font-weight: 500; }
  .foot-head { position: absolute; font-weight: 700; font-size: 12px; letter-spacing: .5px; }
  .foot-text { position: absolute; font-size: 10px; line-height: 16px; color: var(--text-muted); }
  .social { position: absolute; left: 457px; top: 233px; list-style: none; font-size: 10px; color: var(--text-muted); }
  .social li { display: flex; align-items: center; height: 17px; letter-spacing: .4px; }
  .social i { width: 8px; height: 8px; border-radius: 50%; background: var(--text-muted); margin-right: 14px; }
  .email-field { position: absolute; left: 683px; top: 136px; width: 360px; height: 40px; background: var(--input-grey);
    display: flex; align-items: center; padding-left: 16px; font-size: 10px; color: var(--text-muted); letter-spacing: .4px; }
  .email-field svg { position: absolute; right: 12px; top: 14px; }
  .sponsor { position: absolute; top: 270px; width: 59px; height: 57px; border: 2px solid var(--white); }
</style>
</head>
<body>

<div class="photo hero-photo" role="img" aria-label="Conference table with blue cloths, notepads, pens, glasses and water bottles"></div>
<div class="brand">SUMMITWAY</div>
<div class="menu-btn">
  <svg width="18" height="14" viewBox="0 0 18 14"><rect y="0" width="18" height="2.4" fill="#fff"/><rect y="5.8" width="18" height="2.4" fill="#fff"/><rect y="11.6" width="18" height="2.4" fill="#fff"/></svg>
  <span>MENU</span>
</div>
<div class="block hero-card">
  <h1>Amazing Venue’s.<br>Amazing Meetings.</h1>
  <p>Welcome to the personal site of Dana<br>A professional Event Planner.</p>
</div>

<div class="photo about-photo" role="img" aria-label="Portrait of the event planner in a dark blazer outdoors"></div>
<div class="block about-panel">
  <div class="label">ABOUT ME</div>
  <p>Fusce bibendum luctus massa, ut tincidunt lectus tincidunt in. Nulla tristique ipsum vitae lacus ullamcorper, at dictum nunc scelerisque.</p>
</div>

<div class="block why-panel">
  <div class="label">WHY SUMMITWAY</div>
  <p>Etiam lacus dolor, tincidunt vitae nisi in, vulputate placerat odio. Pellentesque iaculis.</p>
  <span class="btn">VIEW OUR SERVICES</span>
</div>
<div class="photo why-photo" role="img" aria-label="Top-down view of people working at a white meeting table"></div>
<div class="block why-fill"></div>

<div class="photo g1" role="img" aria-label="Long banquet table set with lamps and place settings"></div>
<div class="photo g2" role="img" aria-label="Boardroom with a projection screen and conference table"></div>
<div class="photo g3" role="img" aria-label="Speaker addressing an audience in a ballroom"></div>
<div class="photo g4" role="img" aria-label="Lit mountain lodge venue at dusk"></div>

<div class="block blog-left"></div>
<div class="photo blog-art" role="img" aria-label="Illustration of hands using a tablet calendar for an event plan, with charts and papers"></div>
<div class="block blog-card">
  <h2>OUR BLOG</h2>
  <h3>LATEST BLOG POST</h3>
  <p>Lorem Ipsum is simply dummy text of the printing and typesetting industry.</p>
  <span class="btn">CLICK TO PLAY</span>
</div>

<footer class="block footer">
  <div class="foot-brand">SUMMITWAY</div>
  <p class="foot-about">Helping corporate groups find the right venue, negotiate fair contracts and plan meetings that run smoothly from the first call to the final session. Based in the Colorado mountains and happy to travel wherever your team needs to gather. Twenty years of hotel experience, one trusted planner by your side for every detail. Request a proposal today and let us start planning together. Clear plans, honest advice and calm on the day.</p>
  <div class="copyright">©2017. ALL RIGHTS RESERVED.</div>

  <div class="foot-head" style="left:457px;top:47px">CONTACT ME</div>
  <p class="foot-text" style="left:457px;top:78px">88 Aspen Hollow Road<br>Pine Ridge, CO 80400<br><br>Phone: 555-014-2290<br>Email: hello@summitway.example</p>
  <div class="foot-head" style="left:457px;top:210px">FOLLOW ME ON</div>
  <ul class="social">
    <li><i></i>CIRCLEBOOK</li>
    <li><i></i>CHIRPER</li>
    <li><i></i>SNAPGRAM</li>
    <li><i></i>TUNEWAVE</li>
  </ul>

  <div class="foot-head" style="left:683px;top:47px">SUBSCRIBE</div>
  <p class="foot-text" style="left:683px;top:74px;width:360px">Get venue tips, planning checklists and news from the mountains delivered to your inbox once a month. No clutter, just useful ideas for your next meeting.</p>
  <div class="email-field">ENTER YOUR EMAIL ADDRESS
    <svg width="12" height="12" viewBox="0 0 12 12"><path d="M1 6h9M6 2l4 4-4 4" stroke="#8c8e93" stroke-width="1.6" fill="none"/></svg>
  </div>
  <div class="foot-head" style="left:683px;top:241px">SPONSOR</div>
  <div class="sponsor" style="left:681px"></div>
  <div class="sponsor" style="left:756px"></div>
  <div class="sponsor" style="left:833px"></div>
</footer>

</body>
</html>
```